8 x 8 Social Media Design - Crest Pathway #1

Why be a regular Agent, when you can be a Boss?
MOVA PRIMEHOLD REALTY GROUP
We offer Four Levels of Participation
You Increase your Earning Potential at Each Level
Level One - Learn to Earn Additional Income Through....
Mortgage Originations - Dual Licensing / No Additional Work
Real Estate Investing - Invest Jointly with Us
Agent Recruitment - Up to 10% Override
Level Two - Team Leader
Level Three - Minority Mova Franchise Ownership
Level Four - Majority Mova Franchise Ownership
For more information visit us at www.careersatmovaprmhold.example and request a meeting with our Managing Broker, Mr. Harold Tismeer.

```html
<!DOCTYPE html>
<html lang="en">
<head>
<meta charset="utf-8">
<title>Crest Pathway – Be a Boss</title>
<link rel="stylesheet" href="https://fonts.googleapis.com/css2?family=Montserrat:wght@700;800;900&family=Oswald:wght@700&family=Open+Sans:wght@400;600;700&display=swap">
<style>
:root{
  --ink:#2a1a0e;
  --gold:#d6a515;
  --gold-light:#f3cf4a;
  --gold-deep:#9a6d05;
  --brown-dark:#2b1a06;
  --beige:#efe2c8;
  --white:#ffffff;
  --money-light:#eef0ea;
  --money-mid:#cfd6cc;
}
*{box-sizing:border-box;margin:0;padding:0}
html,body{width:1200px;height:1200px;overflow:hidden;background:var(--white)}
.poster{position:relative;width:1200px;height:1200px;overflow:hidden;font-family:"Open Sans",Arial,sans-serif;background:var(--white)}
.abs{position:absolute}

/* hero */
.money-backdrop{left:0;top:60px;width:1200px;height:590px;background:radial-gradient(ellipse at 60% 55%,var(--money-mid),var(--money-light) 70%,var(--white))}
.headline-question{left:45px;top:18px;font-family:"Oswald",sans-serif;font-weight:700;font-size:50px;color:var(--ink);letter-spacing:0.5px;white-space:nowrap}
.when-can-panel{left:728px;top:0;width:472px;height:215px}
.when-you{left:830px;top:14px;font-family:"Montserrat",sans-serif;font-weight:800;font-size:58px;color:var(--white);line-height:1;white-space:nowrap}
.can{left:830px;top:66px;font-family:"Montserrat",sans-serif;font-weight:900;font-size:148px;color:var(--white);line-height:1}
.word-be{left:46px;top:160px;font-family:"Montserrat",sans-serif;font-weight:900;font-size:176px;color:var(--ink);line-height:1;letter-spacing:-4px}
.be-underline{left:51px;top:322px;width:238px;height:20px;background:var(--gold)}
.gold-word{font-family:"Montserrat",sans-serif;font-weight:900;line-height:1;background:linear-gradient(180deg,var(--gold-light),var(--gold) 55%,var(--gold-deep));-webkit-background-clip:text;background-clip:text;color:transparent;white-space:nowrap}
.word-a{left:340px;top:120px;font-size:200px}
.word-boss{left:606px;top:304px;font-size:220px;letter-spacing:-6px;transform:scaleX(0.84);transform-origin:left top}
.broker-photo{left:445px;top:90px;width:330px;height:562px;border-radius:150px 150px 0 0;background:linear-gradient(180deg,#3a3a3f,#1c1c22)}

/* participation */
.we-offer{left:0;top:448px;width:250px;height:46px}
.we-offer-text{left:38px;top:452px;font-family:"Montserrat",sans-serif;font-weight:800;font-size:29px;color:var(--white);white-space:nowrap}
.levels-box{left:0;top:494px;width:460px;height:150px}
.levels-number{left:32px;top:496px;font-family:"Montserrat",sans-serif;font-weight:900;font-size:132px;color:var(--ink);line-height:1}
.levels-label{left:142px;top:524px;font-family:"Montserrat",sans-serif;font-weight:800;font-size:32px;color:var(--white);line-height:1.22;white-space:nowrap}
.earning-band{left:0;top:650px;width:1200px;height:58px;background:var(--white);display:flex;align-items:center;justify-content:center;font-family:"Montserrat",sans-serif;font-weight:800;font-size:34px;color:var(--ink);white-space:nowrap}

/* levels */
.levels-panel{left:0;top:708px;width:1200px;height:492px;background:radial-gradient(ellipse at 50% 60%,#c9980f 0%,#8a5f06 45%,var(--brown-dark) 95%)}
.level-label{top:758px;font-family:"Montserrat",sans-serif;font-weight:700;font-size:22px;color:var(--beige)}
.level-box{top:790px;height:96px;background:var(--beige);display:flex;align-items:center;padding-left:38px;font-family:"Open Sans",sans-serif;font-weight:600;font-size:20px;line-height:1.2;color:var(--ink)}
.level-box.caps{font-family:"Montserrat",sans-serif;font-weight:700;text-transform:uppercase;font-size:19px}
.level-icon{top:781px;width:112px;height:112px}
.income-list{left:128px;top:912px;list-style:none;font-size:22px;line-height:1.22;color:var(--white)}
.income-list li::before{content:"• ";color:var(--gold-light);font-weight:700}
.income-list li.indent::before{content:""}
.income-list .key{color:var(--gold-light);font-family:"Montserrat",sans-serif;font-weight:800;font-size:21px}
.income-list .indent{padding-left:24px}

/* footer */
.footer-band{left:245px;top:1088px;width:955px;height:112px;background:linear-gradient(90deg,#a77608,var(--gold) 60%,#b98a0b)}
.footer-line{left:0;top:1086px;width:1200px;height:6px;background:var(--gold-light)}
.brand-tab{left:0;top:1052px;width:300px;height:148px}
.brand-mark{left:26px;top:1085px;display:flex;align-items:center;gap:12px}
.brand-square{width:34px;height:34px;background:var(--ink)}
.brand-name{font-family:"Montserrat",sans-serif;font-weight:800;font-size:18px;line-height:1.15;color:var(--ink)}
.footer-text{left:296px;top:1120px;font-size:21px;line-height:1.5;color:var(--white);font-weight:600;white-space:nowrap}
.footer-text strong{font-weight:700}
.manager-portrait{left:1038px;top:1021px;width:144px;height:144px;border-radius:50%;border:7px solid var(--gold-light);background:radial-gradient(circle at 50% 40%,#6b5a48,#2a2018)}
</style>
</head>
<body>
<main class="poster">
  <div class="abs money-backdrop" role="img" aria-label="Background of scattered hundred-dollar bills"></div>

  <h1 class="abs headline-question">WHY BE A REGULAR AGENT?</h1>

  <svg class="abs when-can-panel" viewBox="0 0 472 215" aria-hidden="true">
    <polygon points="0,0 472,0 472,215 60,215" fill="var(--gold)"/>
    <polygon points="0,0 60,215 30,215" fill="var(--gold-deep)" opacity="0.5"/>
  </svg>
  <div class="abs when-you">WHEN YOU</div>
  <div class="abs can">CAN</div>

  <div class="abs word-be">BE</div>
  <div class="abs be-underline"></div>
  <div class="abs gold-word word-a">A</div>
  <div class="abs broker-photo" role="img" aria-label="Photo of the broker in a black hat and dark coat, seated with hands clasped"></div>
  <div class="abs gold-word word-boss">BOSS</div>

  <svg class="abs we-offer" viewBox="0 0 250 46" aria-hidden="true"><polygon points="0,0 225,0 250,46 0,46" fill="var(--ink)"/></svg>
  <div class="abs we-offer-text">WE OFFER</div>
  <svg class="abs levels-box" viewBox="0 0 460 150" aria-hidden="true"><polygon points="0,0 405,0 460,150 0,150" fill="var(--gold)"/></svg>
  <div class="abs levels-number">4</div>
  <div class="abs levels-label">LEVELS OF<br>PARTICIPATION</div>

  <div class="abs earning-band">YOU INCREASE YOUR EARNING POTENTIAL AT EACH LEVEL</div>

  <section class="abs levels-panel"></section>

  <div class="abs level-label" style="left:154px">LEVEL 1</div>
  <div class="abs level-label" style="left:475px">LEVEL 2</div>
  <div class="abs level-label" style="left:701px">LEVEL 3</div>
  <div class="abs level-label" style="left:1006px">LEVEL 4</div>

  <div class="abs level-box" style="left:118px;width:226px">Learn to Earn Additional Income Through...</div>
  <div class="abs level-box caps" style="left:430px;width:123px">Team Leader</div>
  <div class="abs level-box caps" style="left:652px;width:210px">Minority Mova Franchise Ownership</div>
  <div class="abs level-box caps" style="left:955px;width:225px">Majority Mova Franchise Ownership</div>

  <svg class="abs level-icon" style="left:29px" viewBox="0 0 112 112" aria-hidden="true">
    <circle cx="56" cy="56" r="54" fill="var(--gold-light)"/><circle cx="56" cy="56" r="44" fill="var(--brown-dark)"/>
    <path d="M56 36a14 14 0 0 0-8 25v6h16v-6a14 14 0 0 0-8-25z" fill="none" stroke="var(--gold-light)" stroke-width="3"/>
    <path d="M49 72h14M51 77h10" stroke="var(--gold-light)" stroke-width="3"/>
    <path d="M56 26v5M38 33l4 4M74 33l-4 4M30 50h5M82 50h-5" stroke="var(--gold-light)" stroke-width="3" stroke-linecap="round"/>
  </svg>
  <svg class="abs level-icon" style="left:349px" viewBox="0 0 112 112" aria-hidden="true">
    <circle cx="56" cy="56" r="54" fill="var(--gold-light)"/><circle cx="56" cy="56" r="44" fill="var(--brown-dark)"/>
    <circle cx="56" cy="44" r="8" fill="var(--gold-light)"/><circle cx="38" cy="50" r="6" fill="var(--gold-light)"/><circle cx="74" cy="50" r="6" fill="var(--gold-light)"/>
    <path d="M42 72a14 14 0 0 1 28 0zM27 70a11 11 0 0 1 18-8M85 70a11 11 0 0 0-18-8" fill="var(--gold-light)"/>
  </svg>
  <svg class="abs level-icon" style="left:571px" viewBox="0 0 112 112" aria-hidden="true">
    <circle cx="56" cy="56" r="54" fill="var(--gold-light)"/><circle cx="56" cy="56" r="44" fill="var(--brown-dark)"/>
    <circle cx="56" cy="56" r="22" fill="var(--gold-light)"/>
    <rect x="40" y="48" width="13" height="7" rx="3" fill="var(--brown-dark)"/><rect x="59" y="48" width="13" height="7" rx="3" fill="var(--brown-dark)"/>
    <path d="M46 63q10 8 20 0" fill="none" stroke="var(--brown-dark)" stroke-width="3" stroke-linecap="round"/>
  </svg>
  <svg class="abs level-icon" style="left:875px" viewBox="0 0 112 112" aria-hidden="true">
    <circle cx="56" cy="56" r="54" fill="var(--gold-light)"/><circle cx="56" cy="56" r="44" fill="var(--brown-dark)"/>
    <text x="56" y="72" text-anchor="middle" font-family="Montserrat, sans-serif" font-weight="900" font-size="46" fill="var(--gold-light)">$</text>
  </svg>

  <ul class="abs income-list">
    <li><span class="key">MORTGAGE ORIGINATIONS</span> -</li>
    <li class="indent">Dual Licensing / No Additional Work</li>
    <li><span class="key">REAL ESTATE INVESTING</span> - Invest Jointly with Us</li>
    <li><span class="key">AGENT RECRUITMENT</span> - Up to 10% Override</li>
  </ul>

  <div class="abs footer-line"></div>
  <div class="abs footer-band"></div>
  <svg class="abs brand-tab" viewBox="0 0 300 148" aria-hidden="true"><polygon points="0,0 250,0 300,148 0,148" fill="var(--white)"/></svg>
  <div class="abs brand-mark">
    <span class="brand-square"></span>
    <span class="brand-name">MOVA PRIMEHOLD<br>REALTY GROUP</span>
  </div>
  <p class="abs footer-text">For more information visit us at <strong>www.careersatmovaprmhold.example</strong><br>and request a meeting with our <strong>Managing Broker, Mr. Harold Tismeer.</strong></p>
  <div class="abs manager-portrait" role="img" aria-label="Round portrait of Managing Broker Harold Tismeer"></div>
</main>
</body>
</html>
```